New Website Design. Porjtect is Guaranteed.

I would like a site similar to this: http://givevehiclehope.org.

old site: http://www.wheelsforbloom.org

Create a professional website; a car donation site seeking leads to return calls.

Please see http://givevehiclehope.org for the concept I am after.

The webpage should have a professional feel. The pages to include are 'Home', 'About us' and 'Get Started'

Industry/Entity Type

It Professional

Coding

Coded - Design and coding required

Number of Pages Required

1 page

```html
<!DOCTYPE html>
<html lang="en">
<head>
<meta charset="utf-8">
<title>Wheels For Bloom – Donate Your Car</title>
<link rel="stylesheet" href="https://fonts.googleapis.com/css2?family=Montserrat:wght@500;600;700&family=Open+Sans:ital,wght@0,400;0,600;0,700;1,400&display=swap">
<style>
:root{
  --navy:#07357f;
  --nav-blue:#0b43a0;
  --section-blue:#0b3f96;
  --title-blue:#0a3a8a;
  --yellow:#f5c300;
  --ink:#1a1a1a;
  --text:#3a3a3a;
  --field-border:#d9b400;
  --card-bg:#fffdf6;
  --card-line:#e6e0c8;
  --white:#ffffff;
}
*{box-sizing:border-box;margin:0;padding:0}
html,body{width:1200px;height:2663px;overflow:hidden;background:var(--white)}
body{font-family:"Open Sans",Arial,sans-serif;color:var(--text)}
.page{position:relative;width:1200px;height:2663px;overflow:hidden}
.abs{position:absolute}
.heading{font-family:"Montserrat",Arial,sans-serif;font-weight:600;color:var(--title-blue)}
.accent-bar{position:absolute;height:6px;background:var(--yellow)}

/* header */
.topbar{left:0;top:0;width:1200px;height:89px;background:var(--navy)}
.brand{left:208px;top:32px;display:flex;align-items:center;gap:8px;font-family:"Montserrat",sans-serif;font-weight:700;font-size:18px;line-height:24px;color:var(--white);white-space:nowrap}
.brand-dot{width:12px;height:12px;border-radius:50%;background:var(--yellow)}
.tagline{left:410px;top:27px;width:260px;text-align:center;font-size:11px;line-height:16px;font-weight:600;color:var(--yellow)}
.navbar{left:0;top:89px;width:1200px;height:36px;background:var(--nav-blue)}
.nav-link{top:98px;font-family:"Open Sans",sans-serif;font-weight:700;font-size:13px;color:var(--white)}

/* hero */
.hero{left:0;top:125px;width:1200px;height:392px;background:linear-gradient(90deg,#e9eaec 0%,#f6f6f6 45%,#eeeeee 100%)}
.hero-car{left:0;top:175px;width:320px;height:340px;background:linear-gradient(135deg,#c9ccd1 0%,#9ea3aa 55%,#4c5057 100%);border-radius:0 140px 30px 0}
.hero-keys{left:440px;top:125px;width:130px;height:230px;background:linear-gradient(180deg,#e8c7b2 0%,#d7b09a 45%,#2c2c2c 100%);border-radius:0 0 50px 50px}
.hero-title{left:330px;top:378px;width:344px;text-align:center;font-size:27px;line-height:33px;font-weight:600}
.hero-title em{font-style:normal;color:var(--yellow)}

/* donation form */
.form-panel{left:687px;top:32px;width:302px;height:485px}
.form-shape{position:absolute;left:0;top:0}
.form-inner{position:absolute;left:0;top:0;width:302px;height:485px}
.form-kicker{position:absolute;top:34px;width:100%;text-align:center;font-size:16px;color:var(--ink)}
.form-phone{position:absolute;top:54px;width:100%;text-align:center;font-family:"Montserrat",sans-serif;font-weight:700;font-size:25px;color:var(--ink)}
.form-divider{position:absolute;left:0;top:98px;width:302px;height:1px;background:#d6a800}
.form-note{position:absolute;top:107px;width:100%;text-align:center;font-size:11px;font-style:italic;font-weight:700;color:var(--ink)}
.field{position:absolute;height:30px;background:var(--white);border:1px solid var(--field-border);font-size:10.5px;font-style:italic;color:#777;padding:8px 8px;line-height:12px}
.field.select::after{content:"";position:absolute;right:8px;top:12px;border:4px solid transparent;border-top:5px solid #555}
.form-subtitle{position:absolute;left:25px;top:308px;font-family:"Montserrat",sans-serif;font-weight:700;font-size:15px;color:var(--ink)}
.form-button{position:absolute;left:25px;top:421px;width:253px;height:36px;background:#181818;color:var(--white);font-family:"Montserrat",sans-serif;font-weight:600;font-size:12px;display:flex;align-items:center;justify-content:center;gap:6px}

/* how it works */
.section-title{font-size:28px;line-height:34px}
.step{position:absolute;top:640px;width:255px;display:flex;gap:12px}
.step-icon{flex:0 0 44px}
.step-title{font-weight:700;font-size:13px;color:var(--yellow);margin-bottom:6px}
.step-text{font-size:10.5px;line-height:17px;color:var(--text)}

/* charities */
.charities{left:0;top:793px;width:1200px;height:482px;background:var(--section-blue)}
.charities-title{left:210px;top:830px;color:var(--yellow)}
.why-card{left:210px;top:900px;width:779px;height:289px;background:var(--white);overflow:hidden}
.why-photo{position:absolute;right:0;top:0;width:460px;height:289px;background:linear-gradient(90deg,rgba(255,255,255,1) 0%,rgba(231,225,214,.6) 20%,#c8b79a 55%,#8b6e55 80%,#b02a2a 100%)}
.why-title{position:absolute;left:30px;top:38px;font-size:19px}
.why-text{position:absolute;left:30px;top:80px;width:355px;font-size:10px;line-height:19px;color:var(--text)}

/* tax */
.tax-title{left:0;top:1316px;width:1200px;text-align:center}
.tax-intro{left:250px;top:1372px;width:700px;text-align:center;font-size:10.5px;line-height:19px}
.tax-card{position:absolute;top:1434px;width:376px;height:194px;background:var(--card-bg);border:1px solid var(--card-line);padding:28px 28px}
.tax-card h3{font-family:"Montserrat",sans-serif;font-weight:600;font-size:16px;line-height:26px;color:var(--yellow);margin-bottom:10px}
.tax-card p{font-size:10.5px;line-height:19px}

/* feature band */
.band{left:0;top:1700px;width:1200px;height:386px;background:linear-gradient(180deg,#f7c900 0%,#f4c000 50%,#f9cf1c 100%)}
.band-bar{left:470px;top:1700px;width:260px;height:6px;background:var(--ink)}
.band-title{left:0;top:1733px;width:1200px;text-align:center;font-family:"Montserrat",sans-serif;font-weight:600;font-size:28px;color:var(--ink)}
.feature{position:absolute;top:1835px;width:200px;text-align:center}
.feature-icon{height:54px;display:flex;justify-content:center;align-items:flex-end;margin-bottom:18px}
.feature-name{font-weight:700;font-size:13.5px;line-height:18px;color:var(--ink);height:40px}
.feature-text{font-size:10.5px;line-height:17px;color:var(--ink);margin-top:6px;padding:0 14px}

/* donate today */
.today{left:0;top:2086px;width:1200px;height:420px;background:linear-gradient(90deg,#f2f2f2 0%,#ebebeb 60%,#dfe3e8 100%)}
.today-photo{left:763px;top:2086px;width:437px;height:420px;background:linear-gradient(120deg,#e9ecf0 0%,#c9b3a0 40%,#4a6ea8 75%,#2b4f8c 100%)}
.today-bar{left:210px;top:2086px;width:262px;height:6px;background:var(--navy)}
.today-title{left:210px;top:2134px;font-size:28px}
.today-text{left:210px;top:2186px;width:385px;font-size:10.5px;line-height:19px}
.perk-list{left:210px;top:2262px;list-style:none}
.perk-list li{font-family:"Montserrat",sans-serif;font-weight:500;font-size:13.5px;line-height:32px;color:var(--ink)}

/* footer */
.footer-line{left:0;top:2506px;width:1200px;height:6px;background:var(--yellow)}
.socials{left:0;top:2549px;width:1200px;display:flex;justify-content:center;gap:9px}
.social-dot{width:25px;height:25px;border-radius:50%;background:var(--yellow)}
.footer-nav{left:0;top:2591px;width:1200px;display:flex;justify-content:center;gap:34px;font-size:12.5px;font-weight:600;color:var(--ink)}
.copyright{left:0;top:2622px;width:1200px;text-align:center;font-size:10px;color:var(--ink)}
.copyright span{margin-left:8px}
</style>
</head>
<body>
<div class="page">

  <!-- header -->
  <div class="abs topbar"></div>
  <div class="abs brand"><span class="brand-dot"></span>Wheels For Bloom</div>
  <div class="abs tagline">Donate Your Car, Truck, RV, Boat, Motorcycle,<br>or ATV in all 50 states to help Veterans.</div>
  <div class="abs navbar"></div>
  <div class="abs nav-link" style="left:211px">Why Donate Your Car</div>
  <div class="abs nav-link" style="left:400px">About</div>
  <div class="abs nav-link" style="left:502px">Our Charity</div>
  <div class="abs nav-link" style="left:628px">Blog</div>

  <!-- hero -->
  <div class="abs hero"></div>
  <div class="abs hero-car" role="img" aria-label="Silver sedan seen from the front corner"></div>
  <div class="abs hero-keys" role="img" aria-label="Hand holding out car keys"></div>
  <h1 class="abs heading hero-title">Donate Car to<br>Children’s <em>Charity!</em></h1>

  <!-- donation form -->
  <div class="abs form-panel">
    <svg class="form-shape" width="302" height="485" viewBox="0 0 302 485">
      <polygon points="0,0 151,14 302,0 302,485 0,485" fill="#f5c300"/>
    </svg>
    <div class="form-inner">
      <div class="form-kicker">Donate Car to Charity!</div>
      <div class="form-phone">1-800-555-0147</div>
      <div class="form-divider"></div>
      <div class="form-note">Or Fill out the form below to instantly donate online</div>
      <div class="field" style="left:25px;top:153px;width:123px">First Name:</div>
      <div class="field" style="left:154px;top:153px;width:124px">Last Name:</div>
      <div class="field" style="left:25px;top:190px;width:253px">Phone:</div>
      <div class="field" style="left:25px;top:227px;width:253px">Email:</div>
      <div class="field" style="left:25px;top:264px;width:123px">Address:</div>
      <div class="field" style="left:154px;top:264px;width:124px">Zip Code:</div>
      <div class="form-subtitle">Vehicle Donation Information</div>
      <div class="field select" style="left:25px;top:341px;width:253px">Year of Vehicle:</div>
      <div class="field select" style="left:25px;top:381px;width:123px">Make of Vehicle:</div>
      <div class="field select" style="left:154px;top:381px;width:124px">Model of Vehicle:</div>
      <div class="form-button">CLICK HERE TO DONATE NOW
        <svg width="11" height="11" viewBox="0 0 12 12"><circle cx="6" cy="6" r="6" fill="#fff"/><path d="M5 3.5 7.5 6 5 8.5" stroke="#181818" stroke-width="1.6" fill="none"/></svg>
      </div>
    </div>
  </div>

  <!-- how it works -->
  <div class="accent-bar" style="left:210px;top:517px;width:258px"></div>
  <h2 class="abs heading section-title" style="left:210px;top:562px">How It Works</h2>

  <div class="step" style="left:210px">
    <svg class="step-icon" width="44" height="60" viewBox="0 0 44 60">
      <rect x="2" y="2" width="36" height="44" fill="#0a3a8a"/>
      <rect x="9" y="12" width="22" height="3" fill="#fff"/><rect x="9" y="20" width="22" height="3" fill="#fff"/><rect x="9" y="28" width="22" height="3" fill="#fff"/>
      <path d="M24 38 L24 56 L28 52 L31 58 L34 57 L31 51 L36 51 Z" fill="#fff" stroke="#0a3a8a" stroke-width="1.5"/>
    </svg>
    <div><div class="step-title">1. Fill out the simple form</div>
    <div class="step-text">Share a few details about your vehicle and we will call you back shortly.</div></div>
  </div>
  <div class="step" style="left:481px">
    <svg class="step-icon" width="44" height="60" viewBox="0 0 44 60">
      <path d="M22 2 V18 M16 16 a6 6 0 1 0 6 -2" stroke="#0a3a8a" stroke-width="3" fill="none"/>
      <path d="M6 42 L10 32 H34 L38 42 V52 H6 Z" fill="#0a3a8a"/>
      <rect x="11" y="35" width="22" height="6" fill="#fff"/>
      <circle cx="12" cy="53" r="4" fill="#0a3a8a"/><circle cx="32" cy="53" r="4" fill="#0a3a8a"/>
    </svg>
    <div><div class="step-title">2. Schedule your free pick-up</div>
    <div class="step-text">Pick a time that suits you and a local driver will collect the car free.</div></div>
  </div>
  <div class="step" style="left:754px">
    <svg class="step-icon" width="44" height="60" viewBox="0 0 44 60">
      <rect x="4" y="2" width="34" height="54" fill="#fff" stroke="#0a3a8a" stroke-width="3"/>
      <path d="M4 56 L38 20 M4 20 L38 56" stroke="#0a3a8a" stroke-width="3"/>
      <rect x="9" y="7" width="11" height="9" fill="#0a3a8a"/><rect x="23" y="9" width="10" height="2" fill="#0a3a8a"/>
    </svg>
    <div><div class="step-title">3. Receive tax deduction</div>
    <div class="step-text">After the sale you get a receipt you can use for your income tax deduction.</div></div>
  </div>

  <!-- charities -->
  <div class="abs charities"></div>
  <div class="accent-bar" style="left:210px;top:793px;width:262px"></div>
  <h2 class="abs heading section-title charities-title">Charities We Work With</h2>
  <div class="abs why-card">
    <div class="why-photo" role="img" aria-label="Woman with arms open beside a red convertible in an open field"></div>
    <h3 class="heading why-title">Why Donate Your Car to Us?</h3>
    <p class="why-text">Every vehicle you give turns into real support for children and families facing hard times. We handle the towing, the paperwork and the sale, so your part takes only a few minutes. Proceeds go straight to the programs we partner with across the country, and you receive the paperwork needed for your tax deduction. Old or new, running or not, your donation counts and helps a child move a little closer to a wish.</p>
  </div>

  <!-- tax -->
  <div class="accent-bar" style="left:470px;top:1275px;width:260px"></div>
  <h2 class="abs heading section-title tax-title">Tax Deduction Information For Your Car Donation</h2>
  <p class="abs tax-intro">The amount you can deduct depends on what your vehicle sells for at auction. The rules below explain how each case works, and we send every donor the forms needed to file.</p>
  <div class="tax-card" style="left:210px">
    <h3>If Your Car Donation Sells for<br>$500 Or Less</h3>
    <p>You may deduct the fair market value of the vehicle up to five hundred dollars. We mail a written receipt within thirty days of the pick-up for your records.</p>
  </div>
  <div class="tax-card" style="left:614px">
    <h3>If Your Car Donation Sells for<br>$501 Or More</h3>
    <p>You may deduct the exact amount the vehicle sold for at auction. We send Form 1098-C with the sale price within thirty days so you can file with ease.</p>
  </div>

  <!-- feature band -->
  <div class="abs band"></div>
  <div class="abs band-bar"></div>
  <h2 class="abs band-title">Donate Car to Charity!</h2>

  <div class="feature" style="left:202px">
    <div class="feature-icon"><div role="img" aria-label="Map of the United States" style="width:76px;height:44px;background:#111;border-radius:10px 18px 14px 22px"></div></div>
    <div class="feature-name">Donations<br>Accepted Nationwide</div>
    <div class="feature-text">We pick up donated vehicles in all fifty states, at no cost to you.</div>
  </div>
  <div class="feature" style="left:397px">
    <div class="feature-icon">
      <svg width="56" height="46" viewBox="0 0 56 46"><path d="M4 22 L10 6 Q11 3 14 3 H42 Q45 3 46 6 L52 22 V38 H4 Z" fill="#111"/><rect x="13" y="9" width="30" height="12" fill="#f5c300"/><circle cx="13" cy="29" r="4" fill="#f5c300"/><circle cx="43" cy="29" r="4" fill="#f5c300"/><rect x="6" y="38" width="9" height="7" fill="#111"/><rect x="41" y="38" width="9" height="7" fill="#111"/></svg>
    </div>
    <div class="feature-name">All Vehicle<br>Types Welcome</div>
    <div class="feature-text">Cars, trucks, boats, RVs, motorcycles and ATVs are all accepted.</div>
  </div>
  <div class="feature" style="left:603px">
    <div class="feature-icon">
      <svg width="40" height="50" viewBox="0 0 40 50"><rect x="3" y="3" width="34" height="44" rx="3" fill="none" stroke="#111" stroke-width="4"/><rect x="10" y="11" width="10" height="3" fill="#111"/><rect x="10" y="19" width="20" height="3" fill="#111"/><rect x="10" y="26" width="20" height="3" fill="#111"/><rect x="10" y="33" width="20" height="3" fill="#111"/></svg>
    </div>
    <div class="feature-name">Tax Deductible</div>
    <div class="feature-text">Your gift qualifies for a deduction on your federal income tax.</div>
  </div>
  <div class="feature" style="left:809px">
    <div class="feature-icon">
      <svg width="64" height="44" viewBox="0 0 64 44"><path d="M2 20 H22 V8 H34 L40 20 V34 H2 Z" fill="#111"/><rect x="25" y="11" width="8" height="8" fill="#f5c300"/><path d="M40 30 L60 10 M60 10 V26" stroke="#111" stroke-width="4" fill="none"/><circle cx="12" cy="36" r="6" fill="#111" stroke="#f5c300" stroke-width="2"/><circle cx="32" cy="36" r="6" fill="#111" stroke="#f5c300" stroke-width="2"/></svg>
    </div>
    <div class="feature-name">Towing is Free</div>
    <div class="feature-text">A local driver collects your vehicle free of charge, on your schedule.</div>
  </div>

  <!-- donate today -->
  <div class="abs today"></div>
  <div class="abs today-photo" role="img" aria-label="Hand passing car keys into an open palm"></div>
  <div class="abs today-bar"></div>
  <h2 class="abs heading today-title">Donate Your Car Today!</h2>
  <p class="abs today-text">Turn the vehicle you no longer need into help for a child in need. Call us or fill out the short form and we take care of the rest, from pick-up to paperwork.</p>
  <ul class="abs perk-list">
    <li>Free Local Towing</li>
    <li>Running or not. Any Condition &amp; Pickup Anywhere.</li>
    <li>Fast Pickup: Same Day to 24 Hours.</li>
    <li>Income Tax Deduction</li>
    <li>No Paperwork Hassles</li>
    <li>Car donations help fund programs</li>
  </ul>

  <!-- footer -->
  <div class="abs footer-line"></div>
  <div class="abs socials">
    <span class="social-dot"></span><span class="social-dot"></span><span class="social-dot"></span><span class="social-dot"></span>
  </div>
  <nav class="abs footer-nav">
    <span>How It Works</span><span>Charities</span><span>Tax Deduction</span><span>FAQ</span><span>Donate Your Car</span>
  </nav>
  <div class="abs copyright">© 2017 All Copyrights are Reserved. <span>Terms of Use</span><span>Privacy Policy</span><span>Sitemap</span></div>

</div>
</body>
</html>
```